A5 Flyer for Financial Services Business

I am after a re-design of our business flyer to fit in with our new branding style and logo colour scheme. Wanting something with a bit of designer flair that I could not create myself. I have included the flyer which I created which lacks style so dazzle me.

I want to use the same content.

Text for main body of flyer is

Are you a small business owner, tradie or PAVC Service Provider struggling to stay on top of your bookkeeping and compliance obligations? If so we would love to help you get back on track and take control of your business finances so that you can make informed business decisions and focus on what you do best.

We have over 20 years industry experience and, as a small business ourselves, we are able to offer our clients a personal bookkeeping solution tailored to meet the needs of your business.

Accounts Payable | Accounts Receivable
Customer Invoicing
Bank and Credit Card Reconciliations
Payroll | Superannuation | Payroll Tax
Business Activity | Instalment Activity Statements
Regular Financial Reports
Xero and Quickbooks Set-Up and Training

```html
<!DOCTYPE html>
<html lang="en">
<head>
<meta charset="utf-8">
<title>Even Keel Financial Services – A5 Flyer</title>
<link href="https://fonts.googleapis.com/css2?family=Source+Sans+3:wght@300;400;600;700&display=swap" rel="stylesheet">
<style>
  :root{
    --board:#5b5b5b;
    --paper:#ffffff;
    --teal:#0e7f86;
    --teal-light:#17a6a3;
    --teal-dark:#0b5d68;
    --slate:#5d5e60;
    --silver:#c9ccce;
    --ink:#222325;
    --photo-a:#c9c3bd;
    --photo-b:#8f8479;
  }
  *{box-sizing:border-box;margin:0;padding:0}
  html,body{width:1200px;height:900px;overflow:hidden}
  body{background:var(--board);font-family:"Source Sans 3",Arial,sans-serif;color:var(--ink);position:relative}
  .flyer{position:absolute;top:108px;width:483px;height:684px;background:var(--paper);overflow:hidden}
  .flyer--team{left:93px}
  .flyer--portrait{left:649px}
  .flyer__shapes{position:absolute;inset:0;width:483px;height:684px}
  .brand{position:absolute;top:30px;right:36px;display:flex;align-items:center;gap:6px;color:var(--teal)}
  .brand__mark{width:12px;height:12px;background:var(--teal)}
  .brand__name{font-weight:300;font-size:14px;line-height:1;letter-spacing:.5px;text-align:center}
  .brand__name small{display:block;font-size:10px;letter-spacing:1.6px;margin-top:2px}
  .pitch{position:absolute;left:245px;top:276px;width:215px;text-align:center}
  .pitch__lead{font-size:15px;font-weight:600;color:var(--slate);line-height:1}
  .pitch__focus{font-size:19px;font-weight:700;color:var(--teal);line-height:1.1;margin-top:3px;letter-spacing:.3px}
  .pitch__title{font-size:50px;font-weight:700;color:var(--slate);line-height:.95;letter-spacing:1px}
  .body-copy{font-size:8.2px;line-height:1.25;text-align:center;color:var(--ink)}
  .pitch .body-copy{margin-top:4px}
  .pitch .body-copy + .body-copy{margin-top:13px}
  .experience{position:absolute;left:28px;top:342px;width:190px;text-align:center}
  .experience__lead{font-size:15px;font-weight:400;color:var(--ink);line-height:1}
  .experience__years{font-size:40px;font-weight:600;color:var(--teal);line-height:1.05;letter-spacing:.5px}
  .experience .body-copy{margin-top:3px}
  .services{position:absolute;list-style:none}
  .services--left{left:33px;top:464px}
  .services--right{left:248px;top:469px}
  .services li{display:flex;align-items:center;height:27px;font-size:8px;font-weight:700;color:var(--ink)}
  .services li::before{content:"";width:12px;height:12px;background:var(--teal);margin-right:17px;flex:none}
  .divider{position:absolute;left:228px;top:462px;width:1px;height:110px;background:var(--silver)}
  .web{position:absolute;right:34px;bottom:26px;font-size:11px;color:#fff;letter-spacing:.3px}
</style>
</head>
<body>

<article class="flyer flyer--team">
  <svg class="flyer__shapes" viewBox="0 0 483 684" aria-hidden="false">
    <defs>
      <linearGradient id="photoTeam" x1="0" y1="0" x2="1" y2="1">
        <stop offset="0" stop-color="#e3e0dc"/><stop offset=".55" stop-color="#b59a84"/><stop offset="1" stop-color="#6f6a70"/>
      </linearGradient>
      <linearGradient id="tealBand" x1="0" y1="0" x2="1" y2="0">
        <stop offset="0" stop-color="#0a5564"/><stop offset="1" stop-color="#139c9a"/>
      </linearGradient>
      <linearGradient id="silverBand" x1="0" y1="0" x2="1" y2="0">
        <stop offset="0" stop-color="#f2f2f2"/><stop offset="1" stop-color="#9ea3a6"/>
      </linearGradient>
    </defs>
    <polygon role="img" aria-label="Photo of smiling businesswomen in a meeting around a table" points="0,0 483,0 483,188 0,318" fill="url(#photoTeam)"/>
    <polygon points="0,326 483,198 483,258 395,250 265,275 0,336" fill="var(--slate)"/>
    <polygon points="0,640 483,560 483,684 0,684" fill="url(#tealBand)"/>
    <polygon points="0,598 150,632 0,664" fill="var(--teal-light)"/>
    <polygon points="110,642 483,578 483,598 175,652" fill="url(#silverBand)"/>
  </svg>
  <div class="brand"><span class="brand__mark"></span><p class="brand__name">EVEN KEEL<small>Financial Services</small></p></div>
  <section class="pitch">
    <p class="pitch__lead">ARE YOU A</p>
    <p class="pitch__focus">SMALL BUSINESS</p>
    <h1 class="pitch__title">OWNER</h1>
    <p class="body-copy">tradie or PAVC Service Provider struggling to stay on top of your bookkeeping and compliance obligations?</p>
    <p class="body-copy">If so we would love to help you get back on track and take control of your business finances so that you can make informed business decisions and focus on what you do best.</p>
  </section>
  <section class="experience">
    <p class="experience__lead">WE HAVE OVER</p>
    <h2 class="experience__years">20 YEARS</h2>
    <p class="body-copy">industry experience and, as a small business ourselves, we are able to offer our clients a personal bookkeeping solution tailored to meet the needs of your business.</p>
  </section>
  <ul class="services services--left">
    <li>Accounts Payable | Accounts Receivable</li>
    <li>Customer Invoicing</li>
    <li>Bank and Credit Card Reconciliations</li>
    <li>Payroll | Superannuation | Payroll Tax</li>
  </ul>
  <div class="divider"></div>
  <ul class="services services--right">
    <li>Accounts Payable | Accounts Receivable</li>
    <li>Customer Invoicing</li>
    <li>Bank and Credit Card Reconciliations</li>
    <li>Payroll | Superannuation | Payroll Tax</li>
  </ul>
  <p class="web">www.evenkeelfinance.com</p>
</article>

<article class="flyer flyer--portrait">
  <svg class="flyer__shapes" viewBox="0 0 483 684">
    <defs>
      <linearGradient id="photoPortrait" x1="0" y1="0" x2="1" y2="1">
        <stop offset="0" stop-color="#dfe7ee"/><stop offset=".45" stop-color="#6d6560"/><stop offset="1" stop-color="#d5dde4"/>
      </linearGradient>
      <linearGradient id="tealBand2" x1="0" y1="0" x2="1" y2="0">
        <stop offset="0" stop-color="#0a5564"/><stop offset="1" stop-color="#139c9a"/>
      </linearGradient>
      <linearGradient id="silverBand2" x1="0" y1="0" x2="1" y2="0">
        <stop offset="0" stop-color="#f2f2f2"/><stop offset="1" stop-color="#9ea3a6"/>
      </linearGradient>
    </defs>
    <polygon role="img" aria-label="Photo of a businesswoman in a dark suit holding a folder in a bright office" points="0,0 483,0 483,188 0,318" fill="url(#photoPortrait)"/>
    <polygon points="0,326 483,198 483,258 395,250 265,275 0,336" fill="var(--slate)"/>
    <polygon points="0,640 483,560 483,684 0,684" fill="url(#tealBand2)"/>
    <polygon points="0,598 150,632 0,664" fill="var(--teal-light)"/>
    <polygon points="110,642 483,578 483,598 175,652" fill="url(#silverBand2)"/>
  </svg>
  <div class="brand"><span class="brand__mark"></span><p class="brand__name">EVEN KEEL<small>Financial Services</small></p></div>
  <section class="pitch">
    <p class="pitch__lead">ARE YOU A</p>
    <p class="pitch__focus">SMALL BUSINESS</p>
    <h1 class="pitch__title">OWNER</h1>
    <p class="body-copy">tradie or PAVC Service Provider struggling to stay on top of your bookkeeping and compliance obligations?</p>
    <p class="body-copy">If so we would love to help you get back on track and take control of your business finances so that you can make informed business decisions and focus on what you do best.</p>
  </section>
  <section class="experience">
    <p class="experience__lead">WE HAVE OVER</p>
    <h2 class="experience__years">20 YEARS</h2>
    <p class="body-copy">industry experience and, as a small business ourselves, we are able to offer our clients a personal bookkeeping solution tailored to meet the needs of your business.</p>
  </section>
  <ul class="services services--left">
    <li>Accounts Payable | Accounts Receivable</li>
    <li>Customer Invoicing</li>
    <li>Bank and Credit Card Reconciliations</li>
    <li>Payroll | Superannuation | Payroll Tax</li>
  </ul>
  <div class="divider"></div>
  <ul class="services services--right">
    <li>Accounts Payable | Accounts Receivable</li>
    <li>Customer Invoicing</li>
    <li>Bank and Credit Card Reconciliations</li>
    <li>Payroll | Superannuation | Payroll Tax</li>
  </ul>
  <p class="web">www.evenkeelfinance.com</p>
</article>

</body>
</html>
```